RM BIZ CARDS

Hi,

Is it possible to see a one sided version (with logo and info) as well as a two-sided version (front side w/logo and back side with info)?
How do we choose card stock and finish once we approve a design?

We would like the following info included:

Peter Lowell
Rosfeld Talent Media
4127 Marwick Lane, Suite 300
Los Angeles, CA 90041
(323) 555-0148
peter@rosfeldtalentmedia.example

```html
<!DOCTYPE html>
<html lang="en">
<head>
<meta charset="utf-8">
<title>Rosfeld Talent Media — Business Cards</title>
<link href="https://fonts.googleapis.com/css2?family=Questrial&display=swap" rel="stylesheet">
<style>
  :root {
    --backdrop: #d9d9d9;
    --paper: #f1f1f1;
    --ink: #141414;
    --black: #050505;
    --red: #e10000;
    --red-ink: #3a0202;
    --white: #ffffff;
  }
  * { margin: 0; padding: 0; box-sizing: border-box; }
  html, body {
    width: 1200px; height: 1200px; overflow: hidden;
    background: var(--backdrop);
    font-family: "Questrial", "Century Gothic", sans-serif;
  }
  .sheet {
    position: relative; width: 1200px; height: 1200px;
  }
  .card {
    position: absolute; left: 240px; width: 720px; height: 411px;
    background: var(--paper); overflow: hidden;
  }
  .card--front { top: 130px; }
  .card--info  { top: 650px; }

  /* brand lockup */
  .brand {
    position: absolute; display: flex; flex-direction: column;
    align-items: center; text-align: center; color: var(--ink);
  }
  .brand__mark {
    width: 54px; height: 54px; border: 3px solid var(--ink);
    border-radius: 50%; margin-bottom: 18px;
  }
  .brand__name {
    font-size: 30px; letter-spacing: 4px; text-transform: uppercase;
    line-height: 1.35;
  }
  .card--front .brand { left: 0; right: 0; top: 112px; }
  .card--front .brand__mark { width: 64px; height: 64px; }
  .card--front .brand__name { font-size: 36px; }

  .card--info .brand { left: 20px; width: 280px; top: 120px; }
  .card--info .brand__name { font-size: 24px; letter-spacing: 3px; }

  /* info panel */
  .info-panel {
    position: absolute; top: 0; right: 0; bottom: 0; left: 300px;
    background: var(--black);
    border-left: 3px solid var(--red);
  }
  .name-tab {
    position: absolute; top: 58px; left: 250px; width: 400px; height: 92px;
    background: var(--red); border-radius: 26px 0 0 26px;
    display: flex; align-items: center; padding-left: 44px;
  }
  .name-tab__text {
    font-size: 46px; color: var(--red-ink); letter-spacing: 0.5px;
  }
  .contact-list {
    position: absolute; left: 330px; top: 186px; list-style: none;
    color: var(--white); font-size: 21px; line-height: 1.3;
  }
  .contact-list li {
    display: flex; align-items: flex-start; gap: 12px; margin-bottom: 14px;
  }
  .contact-list svg { flex: 0 0 18px; margin-top: 5px; }
</style>
</head>
<body>
<main class="sheet">

  <section class="card card--front" aria-label="Card front">
    <div class="brand">
      <span class="brand__mark"></span>
      <p class="brand__name">Rosfeld Talent<br>Media</p>
    </div>
  </section>

  <section class="card card--info" aria-label="Card with contact details">
    <div class="brand">
      <span class="brand__mark"></span>
      <p class="brand__name">Rosfeld Talent<br>Media</p>
    </div>
    <div class="info-panel"></div>
    <div class="name-tab"><h1 class="name-tab__text">Peter Lowell</h1></div>
    <ul class="contact-list">
      <li>
        <svg width="18" height="18" viewBox="0 0 18 18" aria-hidden="true">
          <circle cx="9" cy="9" r="8" fill="none" stroke="var(--red)" stroke-width="2"/>
          <path d="M6 5.5c0 4 2.5 6.5 6.5 6.5l.5-1.8-2-1-1 1c-1.2-.5-2.2-1.5-2.7-2.7l1-1-1-2z" fill="var(--red)"/>
        </svg>
        (323) 555-0148
      </li>
      <li>
        <svg width="18" height="18" viewBox="0 0 18 18" aria-hidden="true">
          <rect x="1" y="4" width="16" height="11" fill="var(--red)"/>
          <path d="M1 4l8 6 8-6" fill="none" stroke="var(--black)" stroke-width="1.5"/>
        </svg>
        peter@rosfeldtalentmedia.example
      </li>
      <li>
        <svg width="18" height="18" viewBox="0 0 18 18" aria-hidden="true">
          <circle cx="9" cy="9" r="6.5" fill="none" stroke="var(--red)" stroke-width="4"/>
        </svg>
        <span>4127 Marwick Lane, Suite 300<br>Los Angeles, CA 90041</span>
      </li>
    </ul>
  </section>

</main>
</body>
</html>
```